Willowmere Therapy (Endure - Renew - Flourish) - Double Sided Business Card

I would like a 2-sided business card. Front: Matte Black or Navy with Logo & Tagline. Back: Name, Address, Phone Number, Email, & Website (maybe would like to include a small map pin-pointing location); Prefer front to be a gold/silver foil (iridescent); Back prefer white or light colored background with lettering that is easy to read and simple

Target Market(s)

Individuals & Couples (13 y.o. - ALL Adults); High end clientele

Industry/Entity Type

Licensed Professional Counselor (Mental Health)

Contact Information for Business Card

Name: Willowmere Therapy; Tagline: Endure - Renew - Flourish; Address: 3175 W. Calder Ave., Suite 842, Fort Worth, TX 76142; Phone: (214) 738-2956; Website: www.WillowmereTherapy.example

Font styles to use
Serif

Requirements
Must have
• Logo on Front (Large) prefer gold/silver foil on a matte dark color (i.e. black, navy, etc.); Back of Card: All other relevant information

```html
<!DOCTYPE html>
<html lang="en">
<head>
<meta charset="utf-8">
<title>Willowmere Therapy – Business Card</title>
<link rel="stylesheet" href="https://fonts.googleapis.com/css2?family=Cinzel:wght@400;500&family=Lora:wght@400&display=swap">
<style>
  :root {
    --backdrop: #5b5b5b;
    --card-dark: #1b1b1b;
    --card-light: #ffffff;
    --gold: #d6b95a;
    --silver: #85848a;
    --ink: #222222;
  }
  * { margin: 0; padding: 0; box-sizing: border-box; }
  html, body { width: 1200px; height: 1195px; overflow: hidden; }
  body { background: var(--backdrop); position: relative; }

  .card {
    position: absolute;
    left: 237px;
    width: 725px;
    height: 440px;
    box-shadow: 6px 8px 14px rgba(0,0,0,0.45);
  }

  /* Front */
  .card-front { top: 137px; background: var(--card-dark); }
  .front-mark {
    position: absolute;
    left: 50%;
    top: 134px;
    width: 60px;
    height: 60px;
    margin-left: -30px;
    border-radius: 50%;
    border: 6px solid var(--gold);
  }
  .front-name {
    position: absolute;
    left: 0; right: 0;
    top: 222px;
    text-align: center;
    font-family: "Cinzel", serif;
    font-weight: 500;
    color: var(--gold);
    font-size: 34px;
    line-height: 1.05;
    letter-spacing: 1px;
  }
  .front-tagline {
    position: absolute;
    left: 0; right: 0;
    top: 290px;
    text-align: center;
    font-family: "Cinzel", serif;
    font-weight: 500;
    color: var(--gold);
    font-size: 13px;
    letter-spacing: 0.5px;
  }

  /* Back */
  .card-back { top: 619px; background: var(--card-light); }
  .back-heading {
    position: absolute;
    left: 58px;
    top: 88px;
    font-family: "Cinzel", serif;
    font-weight: 400;
    color: var(--gold);
    font-size: 26px;
    letter-spacing: 4px;
    white-space: nowrap;
  }
  .back-rule {
    position: absolute;
    left: 60px;
    top: 130px;
    width: 271px;
    height: 1px;
    background: var(--ink);
  }
  .contact-list {
    position: absolute;
    left: 58px;
    top: 254px;
    list-style: none;
  }
  .contact-item {
    display: flex;
    align-items: center;
    height: 31px;
    font-family: "Lora", serif;
    font-size: 14px;
    color: var(--ink);
    letter-spacing: 0.3px;
  }
  .contact-icon { width: 24px; height: 24px; margin-right: 9px; flex: none; }
  .back-mark {
    position: absolute;
    left: 488px;
    top: 130px;
    width: 180px;
    height: 180px;
    border-radius: 50%;
    border: 12px solid var(--silver);
  }
</style>
</head>
<body>

  <section class="card card-front" aria-label="Card front">
    <div class="front-mark"></div>
    <h1 class="front-name">WILLOWMERE<br>THERAPY</h1>
    <p class="front-tagline">ENDURE - RENEW - FLOURISH</p>
  </section>

  <section class="card card-back" aria-label="Card back">
    <h2 class="back-heading">WILLOWMERE THERAPY</h2>
    <div class="back-rule"></div>
    <ul class="contact-list">
      <li class="contact-item">
        <svg class="contact-icon" viewBox="0 0 24 24" aria-hidden="true">
          <path d="M12 2a7 7 0 0 0-7 7c0 5 7 13 7 13s7-8 7-13a7 7 0 0 0-7-7z" fill="var(--gold)"/>
          <circle cx="12" cy="9" r="2.6" fill="#fff"/>
        </svg>
        3175 W. Calder Ave., Suite 842, Fort Worth, TX 76142
      </li>
      <li class="contact-item">
        <svg class="contact-icon" viewBox="0 0 24 24" aria-hidden="true">
          <path d="M6.5 3.5l3 3-2 2.2c1.2 2.6 3.2 4.6 5.8 5.8l2.2-2 3 3-2 2.5c-6.5-.5-12-6-12.5-12.5z" fill="none" stroke="var(--gold)" stroke-width="1.6" stroke-linejoin="round"/>
          <path d="M14 4.5a5.5 5.5 0 0 1 5.5 5.5M14 7.5a2.5 2.5 0 0 1 2.5 2.5" fill="none" stroke="var(--gold)" stroke-width="1.4" stroke-linecap="round"/>
        </svg>
        (214) 738-2956
      </li>
      <li class="contact-item">
        <svg class="contact-icon" viewBox="0 0 24 24" aria-hidden="true">
          <g fill="none" stroke="var(--gold)" stroke-width="1.5">
            <circle cx="12" cy="12" r="10"/>
            <ellipse cx="12" cy="12" rx="4.2" ry="10"/>
            <path d="M2 12h20"/>
          </g>
        </svg>
        www.WillowmereTherapy.example
      </li>
    </ul>
    <div class="back-mark"></div>
  </section>

</body>
</html>
```